Business card for Tolvery Anesthesia LLC

This is for a business care for Tolvery Anesthesia LLC. Dr. Lisbeth Tolvery, CRNA, DNAP is the sole provider in the LLC. Business address is 4718 N Brackley Street,
Oakhaven, PA 17342
CRNA stands for certified registered nurse anesthetist
"Keeping you safe and comfortable"
I plan to give this business card to the patients that I provide anesthesia to.
Creative design that ties into Anesthesia. Calm soothing colors.

Target Market(s)

Business card for my patients.

Industry/Entity Type

Medicine

Contact Information for Business Card

Creative, professional, eye catching

Logo Text

Tolvery Anesthesia

Font styles to use
Serif
Script

Colors

Designer to choose colors to be used in the design.

Requirements
Must have
• Tolvery Anesthesia
• Dr. Lisbeth Tolvery, CRNA, DNAP
• tolvery.anesthesia@ quillmail.net
Nice to have
• "Keeping you safe and comfortable"
Should not have
• phone number

```html
<!DOCTYPE html>
<html lang="en">
<head>
<meta charset="utf-8">
<title>Tolvery Anesthesia — Business Card</title>
<link href="https://fonts.googleapis.com/css2?family=Varela+Round&display=swap" rel="stylesheet">
<style>
  :root {
    --stage: #000000;
    --card-white: #ffffff;
    --teal: #04a88a;
    --ocean: #0284c2;
    --brand-blue: #1a7fc1;
    --brand-green: #1aa882;
    --ink-grey: #6b6b6b;
    --white: #ffffff;
  }
  * { margin: 0; padding: 0; box-sizing: border-box; }
  html, body {
    width: 1200px; height: 1000px; overflow: hidden;
    background: var(--stage);
    font-family: "Varela Round", "Helvetica Neue", Arial, sans-serif;
  }
  .canvas { position: relative; width: 1200px; height: 1000px; }

  .card {
    position: absolute; left: 259px; width: 681px; height: 387px;
    border-radius: 40px; overflow: hidden;
  }

  /* Front */
  .card-front { top: 84px; }
  .front-field {
    position: absolute; inset: 0;
    background: linear-gradient(180deg, var(--teal) 0%, #03999f 50%, var(--ocean) 100%);
  }
  .front-brand {
    position: absolute; left: 0; right: 0; top: 104px;
    text-align: center; color: var(--white);
  }
  .brand-dot {
    display: block; width: 70px; height: 70px; margin: 0 auto 18px;
    border: 4px solid var(--white); border-radius: 50%;
  }
  .front-name { font-size: 36px; line-height: 1; letter-spacing: 0.2px; }
  .front-tagline {
    margin-top: 8px; font-size: 16.5px; letter-spacing: 1.1px; text-transform: uppercase;
  }

  /* Back */
  .card-back { top: 521px; background: var(--card-white); }
  .back-brand {
    position: absolute; left: 0; width: 340px; top: 134px; text-align: center;
  }
  .brand-dot-small {
    display: block; width: 52px; height: 52px; margin: 0 auto 14px;
    border: 3px solid var(--brand-blue); border-radius: 50%;
  }
  .back-name { font-size: 25px; line-height: 1; color: var(--brand-blue); }
  .back-tagline {
    margin-top: 6px; font-size: 12px; letter-spacing: 0.8px;
    color: var(--ink-grey); text-transform: uppercase;
  }
  .divider {
    position: absolute; left: 325px; top: 26px; width: 3px; height: 342px;
    background: linear-gradient(180deg, rgba(0,0,0,0) 0%, rgba(0,0,0,0.22) 50%, rgba(0,0,0,0) 100%);
  }
  .contact { position: absolute; left: 357px; top: 152px; }
  .contact-name { font-size: 24px; color: var(--brand-blue); line-height: 1; }
  .contact-credentials { margin-top: 7px; font-size: 17px; color: var(--brand-green); line-height: 1; }
  .contact-email {
    margin-top: 27px; display: flex; align-items: center; gap: 6px;
    font-size: 16px; color: var(--ink-grey);
  }
  .contact-email svg { flex: none; }
</style>
</head>
<body>
<div class="canvas">
  <section class="card card-front">
    <div class="front-field" role="img" aria-label="Soft teal-to-blue gradient backdrop"></div>
    <div class="front-brand">
      <span class="brand-dot"></span>
      <div class="front-name">Tolvery Anesthesia</div>
      <div class="front-tagline">Keeping you safe and comfortable</div>
    </div>
  </section>

  <section class="card card-back">
    <div class="back-brand">
      <span class="brand-dot-small"></span>
      <div class="back-name">Tolvery Anesthesia</div>
      <div class="back-tagline">Keeping you safe and comfortable</div>
    </div>
    <div class="divider"></div>
    <div class="contact">
      <div class="contact-name">Dr. Lisbeth Tolvery</div>
      <div class="contact-credentials">CRNA, DNAP</div>
      <div class="contact-email">
        <svg width="18" height="13" viewBox="0 0 18 13" aria-hidden="true">
          <rect x="0" y="0" width="18" height="13" fill="#1a7fc1"/>
          <polyline points="1,1 9,7.5 17,1" fill="none" stroke="#ffffff" stroke-width="1.4"/>
          <line x1="1" y1="12" x2="6.5" y2="6" stroke="#ffffff" stroke-width="1.2"/>
          <line x1="17" y1="12" x2="11.5" y2="6" stroke="#ffffff" stroke-width="1.2"/>
        </svg>
        <span>tolvery.anesthesia@quillmail.net</span>
      </div>
    </div>
  </section>
</div>
</body>
</html>
```